Stand out flyer needed for Boxing gym

Hi we need a trifold brochure designed for our outdoor boxing business it will be delivered to doctors and nutritionists to help their patients be healthier and get fit.We have supplied high res pictures for you to use in the brochure. We need a design that use a lot of yellow so it captures their attention. You can check our website for design colours www.punchyard-fit.com.au

Target Market(s)

Overweight or unfit people looking to change their lives

Industry/Entity Type

Health And Wellness

Font styles to use
Sans Serif

Colors
fbee3d
ffffff
000000

Requirements
Must have
• (main heading - large bold font) Get fit lose weight & feel great
• (bold) Unlimited outdoor boxing classes $14.95
• Complete affordability & No judgements guaranteed
• (bold) Tailored programs (bold)
• Our programs are structured so that members of all fitness levels feel confident & comfortable during their start-up phase allowing you to quickly build your fitness
• (bold) Injury prevention (bold)
• Our training systems include techniques that will help you avoid injuries and build balanced strength
• (bold) Strengthen & Tone your core (bold)
• You're core muscles are some of you're most important muscles. Each workout you do incorporates core exercises to help avoid injuries and make you're total body stronger
• (bold) Wake up with more energy(bold)
• Every class you'll do will have you filled with energy the will pump you up for the rest of your day
• (bold) Sleep better(bold)
• One of the best parts of exercise is the benefit it has on your sleeping patterns. You'll sleep deeper & more sound
• (bold) Supportive environment (bold)
• At JAB YARD you'll be surrounded by trainers & other members who are there to encourage & motivate you to reach your goals and to get you moving more.
• Coupon code: SwingHigh27

```html
<!DOCTYPE html>
<html lang="en">
<head>
<meta charset="utf-8">
<title>JAB YARD Trifold Brochure</title>
<link href="https://fonts.googleapis.com/css2?family=Bebas+Neue&family=Open+Sans:wght@400;600;700&display=swap" rel="stylesheet">
<style>
:root{
  --yellow:#fbee3d;
  --white:#ffffff;
  --black:#000000;
  --ink:#2b2b2b;
  --stage:#d5d6d8;
  --band:#4a4a4a;
}
*{margin:0;padding:0;box-sizing:border-box}
html,body{width:827px;height:1200px;overflow:hidden;background:var(--stage)}
body{position:relative;font-family:"Open Sans",Arial,sans-serif}
.head{font-family:"Bebas Neue","Oswald",sans-serif;font-weight:400;letter-spacing:.3px;line-height:1;white-space:nowrap}
.panel{position:absolute;left:73px;width:693px;height:490px;overflow:hidden;box-shadow:0 14px 14px -8px rgba(0,0,0,.35)}
.outside{top:82px;background:linear-gradient(100deg,#2c2c2c 0%,#151515 40%,#262626 70%,#121212 100%)}
.inside{top:632px;background:linear-gradient(90deg,#1f1f1f,#2e2e2e 60%,#1a1a1a)}
.shapes{position:absolute;left:0;top:0;width:693px;height:490px}
.abs{position:absolute}

/* outside: offer column */
.price{left:26px;top:62px;font-size:36px;color:var(--yellow)}
.offer{left:26px;top:106px;font-size:22px;color:var(--white);line-height:1.1}
.promise{left:26px;top:168px;font-size:10.5px;color:var(--white);line-height:1.45}
.coupon{left:20px;top:221px;width:191px;height:38px;border-radius:19px;background:var(--yellow);border:2px solid var(--white);display:flex;align-items:center;justify-content:center;font-size:16px;color:var(--black)}

/* outside: contact column */
.brand-mid{left:232px;width:229px;top:44px;text-align:center;font-size:36px;color:var(--yellow);letter-spacing:2px}
.contact-title{left:232px;width:229px;top:103px;text-align:center;font-size:20px;color:var(--white);line-height:1.12}
.map{left:278px;top:165px;width:134px;height:134px;border-radius:50%;background:radial-gradient(circle,#e6e6e6,#c9c9c9);border:4px solid var(--white)}
.locations{left:275px;top:313px;color:var(--white)}
.loc-name{font-family:"Bebas Neue",sans-serif;font-size:12px;color:var(--yellow);line-height:1}
.loc-addr{font-size:7.5px;margin-bottom:8px;line-height:1.2;white-space:nowrap}
.phone{left:232px;width:229px;top:432px;text-align:center;font-size:14px;color:var(--yellow);line-height:1.3}

/* outside: cover column */
.brand-cover{left:511px;width:132px;top:29px;text-align:center;font-size:36px;color:var(--white);letter-spacing:2px}
.headline{left:480px;width:200px;top:88px;text-align:center;font-size:26px;color:var(--yellow);line-height:1.12}
.url-band{left:498px;top:428px;width:195px;height:34px;background:var(--yellow);display:flex;align-items:center;justify-content:center;font-weight:700;font-size:12px;color:var(--black);white-space:nowrap}

/* inside */
.tab{left:0;top:31px;width:150px;height:34px;background:var(--black);border-radius:0 17px 17px 0;display:flex;align-items:center;padding-left:16px;font-size:17px;color:var(--yellow)}
.copy{font-size:11.4px;line-height:1.3}
.light .copy{color:var(--ink)}
.light-title{font-size:19px;color:#1c1c1c}
.dark-title{font-size:19px;color:var(--white)}
.accent-title{font-size:19px;color:var(--yellow)}
.dark .copy{color:#e8e8e8}
.strap{left:0;top:401px;width:398px;height:36px;background:var(--band);display:flex;align-items:center;padding-left:18px;font-size:18px;color:var(--white)}
.url-foot{left:23px;top:449px;font-weight:700;font-size:15px;color:var(--black);white-space:nowrap}
</style>
</head>
<body>

<section class="panel outside">
  <svg class="shapes" viewBox="0 0 693 490">
    <defs>
      <linearGradient id="coverPhoto" x1="0" y1="0" x2="0" y2="1">
        <stop offset="0" stop-color="#4a4a4a"/>
        <stop offset="1" stop-color="#1c1c1c"/>
      </linearGradient>
    </defs>
    <path role="img" aria-label="Photo of a woman stretching outdoors in a sunlit park" d="M0,300 C120,292 215,338 258,490 L0,490 Z" fill="#5f6a45"/>
    <path d="M0,280 C135,262 240,318 272,490 L258,490 C215,338 120,292 0,300 Z" fill="#fbee3d"/>
    <path role="img" aria-label="Black and white photo of a female boxer in guard stance" d="M693,168 C612,222 540,292 540,382 C540,428 546,462 556,490 L693,490 Z" fill="url(#coverPhoto)"/>
    <path d="M693,148 C598,206 524,282 524,384 C524,432 532,466 545,490 L556,490 C546,462 540,428 540,382 C540,292 612,222 693,168 Z" fill="#fbee3d"/>
  </svg>

  <div class="abs head price">$14.95</div>
  <div class="abs head offer">UNLIMITED OUTDOOR<br>BOXING CLASSES</div>
  <div class="abs promise">Complete affordability &amp;<br>No judgements guaranteed!</div>
  <div class="abs head coupon">COUPON CODE: SWINGHIGH27</div>

  <div class="abs head brand-mid">JAB YARD</div>
  <div class="abs head contact-title">CONTACT US TODAY<br>FOR MORE INFORMATION</div>
  <div class="abs map" role="img" aria-label="Street map marking the four class locations"></div>
  <div class="abs locations">
    <div class="loc-name">ASHGROVE</div>
    <div class="loc-addr">12-18 Kestrel Rd, Ashgrove</div>
    <div class="loc-name">WILLOWBANK</div>
    <div class="loc-addr">Willowbank NSW 2901</div>
    <div class="loc-name">FERNHILL</div>
    <div class="loc-addr">410 Ridge St, Fernhill NSW 2902</div>
    <div class="loc-name">CORAL BAY</div>
    <div class="loc-addr">77-81 Tidal Rd, Coral Bay NSW 2903</div>
  </div>
  <div class="abs head phone">0400 123 987<br>INFO@PUNCHYARD-FIT.COM.AU</div>

  <div class="abs head brand-cover">JAB YARD</div>
  <div class="abs head headline">GET FIT LOSE WEIGHT<br>&amp; FEEL GREAT</div>
  <div class="abs url-band">www.punchyard-fit.com.au</div>
</section>

<section class="panel inside">
  <svg class="shapes" viewBox="0 0 693 490">
    <defs>
      <linearGradient id="fadeLeft" x1="0" y1="0" x2="1" y2="1">
        <stop offset="0" stop-color="#ffffff"/>
        <stop offset=".55" stop-color="#f1f1f1"/>
        <stop offset="1" stop-color="#b9b9b9"/>
      </linearGradient>
    </defs>
    <path role="img" aria-label="Faded photo of a boxer training in front of a city skyline" d="M0,0 L212,0 C222,90 238,150 275,210 C320,285 420,330 446,420 C452,445 450,470 448,490 L0,490 Z" fill="url(#fadeLeft)"/>
    <path d="M238,0 C248,90 264,150 301,210 C346,285 446,330 472,420 C478,445 476,470 474,490 L448,490 C450,470 452,445 446,420 C420,330 320,285 275,210 C238,150 222,90 212,0 Z" fill="#000000"/>
    <path d="M226,0 C236,90 252,150 289,210 C334,285 434,330 460,420 C466,445 464,470 462,490 L448,490 C450,470 452,445 446,420 C420,330 320,285 275,210 C238,150 222,90 212,0 Z" fill="#fbee3d"/>
    <path role="img" aria-label="Photo of a smiling woman exercising on grass" d="M480,490 C532,400 606,345 693,318 L693,490 Z" fill="#4f5c3c"/>
    <path d="M466,490 C520,392 600,330 693,302 L693,318 C606,345 532,400 480,490 Z" fill="#fbee3d"/>
  </svg>

  <div class="light">
    <div class="abs head tab">TAILORED PROGRAMS</div>
    <p class="abs copy" style="left:18px;top:80px;width:215px">Our programs are structured so that members of all fitness levels feel confident &amp; comfortable during their start-up phase allowing you to quickly build your fitness</p>
    <div class="abs head light-title" style="left:18px;top:190px">INJURY PREVENTION</div>
    <p class="abs copy" style="left:18px;top:214px;width:260px">Our training systems include techniques that will help you avoid injuries and build balanced strength</p>
    <div class="abs head light-title" style="left:18px;top:286px">STRENGTHEN &amp; TONE YOUR CORE</div>
    <p class="abs copy" style="left:18px;top:310px;width:275px">You're core muscles are some of you're most important muscles. Each workout you do incorporates core exercises to help avoid injuries and make you're total body stronger</p>
    <div class="abs head strap">COMPLETE AFFORDABILITY &amp; NO JUDGEMENTS GUARANTEED!</div>
    <div class="abs url-foot">www.punchyard-fit.com.au</div>
  </div>

  <div class="dark">
    <div class="abs head accent-title" style="left:265px;width:180px;top:42px;text-align:center">WAKE UP WITH MORE ENERGY</div>
    <p class="abs copy" style="left:272px;width:172px;top:74px;text-align:center">Every class you'll do will have you filled with energy the will pump you up for the rest of your day</p>
    <div class="abs head dark-title" style="left:483px;top:42px">SLEEP BETTER</div>
    <p class="abs copy" style="left:483px;top:74px;width:192px">One of the best parts of exercise is the benefit it has on your sleeping patterns. You'll sleep deeper &amp; more sound</p>
    <div class="abs head dark-title" style="left:483px;top:165px">SUPPORTIVE ENVIRONMENT</div>
    <p class="abs copy" style="left:483px;top:197px;width:192px">At JAB YARD you'll be surrounded by trainers &amp; other members who are there to encourage &amp; motivate you to reach your goals and to get you moving more.</p>
  </div>
</section>

</body>
</html>
```